Dale Porcher Announces his new career move! 8x5 card please.

Associate Broker DALE PORCHER is proud to announce his new affiliation with m.voller sandy cove homes, ltd.

His goal remains to meet all your real estate needs. Prepare to renew your seasonal rental for 2016...with the full support of his new office, Dale can handle your renewal seamlessly.

Prepared to purchase? With access to every property on the market...Dale can show you how easy it making your summer dreams come true can be.

Thinking about selling? m.voller sandy cove homes, ltd. now offers the benefits of the Shared Offering Registry (SOR) to all sellers. In cooperation with SOR Sellers receive the maximum worldwide exposure, Purchasers receive a larger volume of properties to view and in cooperation with other Realtors, the transaction is handled professionally!!!!

I will send logo and photo of Dale Porcher separately. Thank you. M-
Updates

Project Deadline Extended Reason: I would need the cards to be delivered to my office by Friday June 26th for delivery to the public on the 27th. Thank you. Added Wednesday, June 17, 2015

Target Market(s)

Tenants, Sellers & Buyers

Industry/Entity Type

Broker

Font styles to use
Sans Serif

Requirements
Must have
• I attached logo and photo of Dale. Added a better photo of Dale.
Nice to have
• A photo of a property we have listed. I added a couple to choose from.
Should not have
• No Red color

```html
<!DOCTYPE html>
<html lang="en">
<head>
<meta charset="utf-8">
<title>Dale Porcher – Announcement Postcard</title>
<link href="https://fonts.googleapis.com/css2?family=Open+Sans:wght@300;400;600;700&display=swap" rel="stylesheet">
<style>
  :root {
    --green: #137a4c;
    --charcoal: #3c3d3f;
    --panel-grey: #d5d6d8;
    --panel-text: #505254;
    --paper: #ffffff;
    --back-grey: #e8e9eb;
    --stamp: #9c9ea1;
    --line: #8d8f92;
    --backdrop: #f0f0f0;
  }
  * { margin: 0; padding: 0; box-sizing: border-box; }
  html, body { width: 860px; height: 1200px; overflow: hidden; }
  body {
    background: var(--backdrop);
    font-family: "Open Sans", Arial, sans-serif;
    position: relative;
  }
  .card {
    position: absolute;
    left: 82px;
    width: 713px;
    height: 508px;
    overflow: hidden;
    box-shadow: 0 3px 10px rgba(0,0,0,.25);
  }

  /* ---------- Front ---------- */
  .front { top: 92px; background: var(--paper); }
  .front-shape { position: absolute; inset: 0; }
  .wordmark {
    position: absolute;
    font-weight: 600;
    letter-spacing: -0.5px;
    white-space: nowrap;
  }
  .front-wordmark {
    left: 44px; top: 40px;
    font-size: 31px;
    color: var(--charcoal);
  }
  .wordmark-mark {
    position: absolute;
    left: 565px; top: 38px;
    width: 40px; height: 40px;
    border-radius: 50%;
    background: var(--green);
  }
  .announce-panel {
    position: absolute;
    left: 25px; top: 148px;
    width: 211px; height: 293px;
    background: var(--panel-grey);
    box-shadow: 2px 3px 6px rgba(0,0,0,.35);
    text-align: center;
    color: var(--panel-text);
    padding: 8px 10px 0;
  }
  .announce-title {
    font-size: 19.5px;
    font-weight: 600;
    line-height: 25px;
  }
  .announce-title strong { font-weight: 700; }
  .announce-body {
    margin-top: 24px;
    font-size: 11px;
    font-weight: 700;
    line-height: 17px;
  }
  .pitch {
    position: absolute;
    left: 264px;
    width: 416px;
    color: #fff;
  }
  .pitch h2 { font-size: 16px; font-weight: 700; margin-bottom: 8px; }
  .pitch p { font-size: 11.5px; line-height: 16.5px; text-align: justify; }
  .pitch-buy { top: 228px; }
  .pitch-sell { top: 330px; }
  .contact-line {
    position: absolute;
    left: 26px; top: 476px;
    font-size: 15px; font-weight: 700; color: #fff;
  }
  .web-tab {
    position: absolute;
    left: 405px; top: 473px;
    width: 282px; height: 33px;
  }
  .web-tab span {
    position: absolute;
    left: 24px; top: 6px;
    font-size: 16px; font-weight: 700; color: var(--charcoal);
  }

  /* ---------- Back ---------- */
  .back { top: 628px; background: var(--back-grey); }
  .back-topbar { position: absolute; left: 0; top: 0; width: 713px; height: 10px; background: #111; }
  .address-side { position: absolute; left: 426px; top: 10px; width: 287px; height: 498px; background: #efeff0; }
  .back-header {
    position: absolute; left: 0; top: 12px; width: 426px; height: 54px;
    background: var(--charcoal); color: #fff;
    font-size: 22px; font-weight: 300; padding: 12px 0 0 24px;
    white-space: nowrap;
  }
  .back-header strong { font-weight: 700; }
  .back-green { position: absolute; left: 0; top: 66px; width: 426px; height: 344px; background: var(--green); }
  .property-photo { position: absolute; top: 9px; height: 99px; }
  .property-photo.kitchen { left: 10px; width: 133px; background: linear-gradient(135deg,#6b4a2e,#b99a78 60%,#d9d3c8); }
  .property-photo.pool { left: 146px; width: 131px; background: linear-gradient(180deg,#7fb3e0 0%,#e8eef2 45%,#2aa6d8 75%,#1e6fa3); }
  .property-photo.bedroom { left: 280px; width: 133px; background: linear-gradient(135deg,#e9ece9,#a8b8a2 55%,#c98a7a); }
  .back-wordmark {
    left: 18px; top: 186px;
    font-size: 25px;
    color: #fff;
  }
  .agent {
    position: absolute; right: 460px; top: 278px; width: 240px;
    text-align: right; color: #fff;
  }
  .agent-name { font-size: 21px; font-weight: 700; line-height: 26px; }
  .agent-title { font-size: 18px; font-weight: 300; line-height: 24px; margin-bottom: 14px; }
  .agent-office { font-size: 12px; font-weight: 700; line-height: 16px; }
  .agent-address { font-size: 12px; line-height: 16px; }
  .agent-photo {
    position: absolute; left: 275px; top: 171px; width: 121px; height: 146px;
    border-radius: 8px; border: 1px solid rgba(255,255,255,.5);
    background: linear-gradient(180deg,#b9c3c9 0%,#9aa6ab 50%,#3a3030 100%);
  }
  .back-contact {
    position: absolute; left: 0; top: 410px; width: 426px; height: 25px;
    background: var(--charcoal); color: #fff; font-size: 14px; font-weight: 700;
    padding: 3px 0 0 28px; word-spacing: 1px; white-space: nowrap;
  }
  .back-contact span + span { margin-left: 26px; }
  .postal-note { position: absolute; left: 122px; top: 465px; font-size: 10px; font-weight: 600; color: #222; }
  .stamp-box { position: absolute; left: 585px; top: 32px; width: 104px; height: 108px; border-radius: 8px; background: var(--stamp); }
  .address-line { position: absolute; left: 450px; width: 233px; height: 1px; background: var(--line); }
</style>
</head>
<body>

<section class="card front">
  <svg class="front-shape" viewBox="0 0 713 506" width="713" height="506" aria-hidden="true">
    <defs>
      <linearGradient id="silverBand" x1="0" y1="0" x2="1" y2="0">
        <stop offset="0" stop-color="#c9cbce"/>
        <stop offset=".5" stop-color="#f4f4f5"/>
        <stop offset="1" stop-color="#a9abae"/>
      </linearGradient>
      <linearGradient id="tabSilver" x1="0" y1="0" x2="0" y2="1">
        <stop offset="0" stop-color="#f5f5f6"/>
        <stop offset="1" stop-color="#b5b7ba"/>
      </linearGradient>
    </defs>
    <path d="M0,118 C150,98 300,138 420,158 C520,176 600,180 648,136 C676,108 700,74 713,54 L713,506 L0,506 Z" fill="url(#silverBand)"/>
    <path d="M0,133 C150,113 300,153 420,172 C520,190 600,194 652,152 C682,124 702,90 713,72 L713,506 L0,506 Z" fill="var(--green)"/>
    <path d="M395,506 L417,473 L675,473 Q683,490 690,506 Z" fill="url(#tabSilver)"/>
  </svg>

  <div class="wordmark front-wordmark">m.voller sandy cove homes, ltd.</div>
  <div class="wordmark-mark"></div>

  <div class="announce-panel">
    <p class="announce-title">Associate Broker <strong>DALE PORCHER</strong> is proud to announce his new affiliation with <strong>m.voller</strong> sandy cove homes, ltd.</p>
    <p class="announce-body">His goal remains to meet all your real estate needs. Prepare to renew your seasonal rental for 2016...with the full support of his new office, Dale can handle your renewal seamlessly.</p>
  </div>

  <div class="pitch pitch-buy">
    <h2>Prepared to purchase?</h2>
    <p>With access to every property on the market...Dale can show you how easy it making your summer dreams come true can be.</p>
  </div>
  <div class="pitch pitch-sell">
    <h2>Thinking about selling?</h2>
    <p>m.voller sandy cove homes, ltd. now offers the benefits of the Shared Offering Registry (SOR) to all sellers. In cooperation with SOR Sellers receive the maximum worldwide exposure, Purchasers receive a larger volume of properties to view and in cooperation with other Realtors, the transaction is handled professionally!!!!</p>
  </div>

  <div class="contact-line">Contact us: 555.210.4400, 555.318.2290 (Dale)</div>
  <div class="web-tab"><span>www.sandycovehomes.com</span></div>
</section>

<section class="card back">
  <div class="back-topbar"></div>
  <div class="address-side"></div>
  <div class="back-header">the fabulous homes of <strong>sandy cove</strong></div>

  <div class="back-green">
    <div class="property-photo kitchen" role="img" aria-label="Property photo: modern wood kitchen"></div>
    <div class="property-photo pool" role="img" aria-label="Property photo: house with swimming pool"></div>
    <div class="property-photo bedroom" role="img" aria-label="Property photo: bright bedroom"></div>
    <div class="agent-photo" role="img" aria-label="Portrait photo of Dale Porcher"></div>
  </div>

  <div class="wordmark back-wordmark">m.voller sandy cove homes, ltd.</div>

  <div class="agent">
    <p class="agent-name">DALE PORCHER</p>
    <p class="agent-title">Associate Broker</p>
    <p class="agent-office">m.voller sandy cove homes, ltd.</p>
    <p class="agent-address">on the harbor, P.O. Box 4127,<br>Sandy Cove, NY 10990</p>
  </div>

  <div class="back-contact"><span>fax: 555-210-4405</span><span>e-mail: info@sandycovehomes.com</span></div>
  <p class="postal-note">barcode &amp; postal marketing area</p>

  <div class="stamp-box"></div>
  <div class="address-line" style="top:329px"></div>
  <div class="address-line" style="top:365px"></div>
  <div class="address-line" style="top:402px"></div>
  <div class="address-line" style="top:438px"></div>
</section>

</body>
</html>
```